KTR Business Card

We need a new design for our business cards. We are brokers in the scrap metal industry and wants something nice, clean and very professional.

Industry/Entity Type

Business

Requirements
Must have
• Our logo
• Would probably be good to incorporate colors from logo into design.
• Example info we need on the cards.
• Name
• Company Address
• Cell Phone
• Office Phone
• Fax
• Email
• Company Website
Should not have
• Should not be too cluttered. Needs to be nice, clean and professional looking.

```html
<!DOCTYPE html>
<html lang="en">
<head>
<meta charset="utf-8">
<title>KTR Business Card</title>
<link href="https://fonts.googleapis.com/css2?family=Exo+2:wght@400;500&family=Roboto+Condensed:wght@700&display=swap" rel="stylesheet">
<style>
  :root {
    --page: #e9e7e3;
    --card: #ffffff;
    --panel: #3b3b3d;
    --accent: #1d8fd2;
    --ink: #2b2b2d;
    --light: #ffffff;
  }
  html, body {
    margin: 0;
    width: 1200px;
    height: 1085px;
    overflow: hidden;
    background: var(--page);
  }
  .card {
    position: absolute;
    left: 75px;
    top: 242px;
    width: 1050px;
    height: 600px;
    background: linear-gradient(135deg, #ffffff 0%, #f1f1f1 100%);
    box-shadow: 0 10px 30px rgba(0,0,0,.18);
    overflow: hidden;
    font-family: "Exo 2", sans-serif;
  }
  .contact-panel {
    position: absolute;
    inset: 0;
  }
  .contact-list {
    position: absolute;
    left: 0;
    top: 0;
    width: 380px;
    height: 600px;
    margin: 0;
    padding: 0;
    list-style: none;
    color: var(--light);
    font-size: 27px;
    line-height: 1.25;
    letter-spacing: 1px;
    text-align: right;
  }
  .contact-list li {
    position: absolute;
    right: 0;
    transform: translateY(-50%);
  }
  .contact-phone   { top: 150px; }
  .contact-address { top: 300px; }
  .contact-web     { top: 450px; }
  .brand {
    position: absolute;
    left: 560px;
    top: 120px;
    display: flex;
    align-items: center;
    gap: 18px;
  }
  .brand-mark {
    width: 26px;
    height: 26px;
    background: var(--accent);
  }
  .brand-name {
    font-family: "Roboto Condensed", sans-serif;
    font-weight: 700;
    font-size: 40px;
    color: var(--ink);
  }
  .person {
    position: absolute;
    left: 640px;
    top: 330px;
  }
  .person-name {
    margin: 0;
    font-weight: 400;
    font-size: 38px;
    letter-spacing: 3px;
    color: var(--accent);
  }
  .person-role {
    margin: 4px 0 0;
    font-size: 27px;
    letter-spacing: 1px;
    color: var(--ink);
  }
</style>
</head>
<body>
  <div class="card">
    <svg class="contact-panel" width="1050" height="600" viewBox="0 0 1050 600" aria-hidden="true">
      <path fill="var(--panel)" d="M0 0 H395
        C395 60 480 80 480 150 C480 220 400 225 400 235
        C400 245 480 240 480 300 C480 360 400 365 400 375
        C400 385 480 390 480 450 C480 520 395 540 395 600
        H0 Z"/>
      <g fill="none" stroke="var(--accent)" stroke-width="3">
        <circle cx="440" cy="150" r="24"/>
        <circle cx="440" cy="300" r="24"/>
        <circle cx="440" cy="450" r="24"/>
        <!-- phone -->
        <path d="M431 140 q-3 10 4 18 q7 7 16 4 l-1 -5 l-6 -2 l-3 3 q-6 -3 -8 -9 l3 -3 l-2 -6 z" stroke-linejoin="round"/>
        <!-- pin -->
        <path d="M440 315 C432 305 430 299 430 294 a10 10 0 0 1 20 0 c0 5 -2 11 -10 21 z"/>
        <circle cx="440" cy="294" r="3.5"/>
        <!-- globe -->
        <circle cx="440" cy="450" r="13"/>
        <ellipse cx="440" cy="450" rx="6" ry="13"/>
        <line x1="427" y1="450" x2="453" y2="450"/>
        <line x1="430" y1="443" x2="450" y2="443"/>
        <line x1="430" y1="457" x2="450" y2="457"/>
      </g>
    </svg>

    <ul class="contact-list">
      <li class="contact-phone">012 555 0147<br>012 555 0147</li>
      <li class="contact-address">042.12th floor,<br>Harbor Point Road<br>KTN</li>
      <li class="contact-web">info@ktrmail.com<br>ktrtrading.com</li>
    </ul>

    <div class="brand">
      <span class="brand-mark"></span>
      <span class="brand-name">Keystone Trade Recycling</span>
    </div>

    <div class="person">
      <h1 class="person-name">DANIEL MORROW</h1>
      <p class="person-role">Managing Director</p>
    </div>
  </div>
</body>
</html>
```